依頼概要
■依頼の目的/概要
コンサルティング業の中で「ほたる相談室」というテーマの中で、
営業力や対人対応力の向上支援などをお手伝いしています。
今回電子書籍出版にあたり、添付ファイルの書籍のイメージに沿うデザインを製作依頼させていただきます。

■書籍タイトル:『どうして?腕時計を磨くと来店客がふえるのか』
サブタイトル:「未来をひらくのは話術より笑顔力」

■本の内容
見た目が人に与える印象などについて記載したものになります。
営業マンのような個人の方や、法人教育に携わるような方にもお読みいただきたいものです。
詳細は添付ファイルを参照ください。

■デザイン要望
自由なご提案をおまちしております。
堅苦しくなく、気軽に手に取っていただけるようなデザインを希望です。

その他何かご不明な点がございましたら、お気軽にご質問下さい。
よろしくお願いいたします。
提案して頂いた皆様、私のミスで写真を2枚お送りできていませんでした。
大変申し訳ございませんがこの写真2枚を使って頂けますよう宜しくお願い致します。

この写真を使ってください
■ 選んだ理由

ネクタイの縦とメッセージの流れがとても良かったです。

■ 提案者全員のお礼・コメント

今回は、沢山の人にいろいろなデザインでご提案いただきありがとうございました。

```html
<!DOCTYPE html>
<html lang="ja">
<head>
<meta charset="utf-8">
<title>どうして?腕時計を磨くと来店客がふえるのか</title>
<link rel="stylesheet" href="https://fonts.googleapis.com/css2?family=Noto+Sans+JP:wght@500;700;900&display=swap">
<style>
  :root {
    --navy: #1c2c6b;
    --navy-deep: #14205a;
    --green: #2f9a3a;
    --red: #d8232a;
    --white: #ffffff;
    --ink: #1b1b1b;
    --photo-a: #e9ebee;
    --photo-b: #c9ccd2;
    --figure-a: #5a5d63;
    --figure-b: #3b3e44;
  }
  html, body { margin: 0; padding: 0; overflow: hidden; }
  body { width: 748px; height: 1200px; font-family: "Noto Sans JP", sans-serif; }
  .cover { position: relative; width: 748px; height: 1200px; background: var(--white); overflow: hidden; }

  .subtitle-band { position: absolute; left: 0; top: 0; width: 748px; height: 62px; background: var(--white);
    display: flex; align-items: center; padding-left: 22px; box-sizing: border-box; z-index: 2; }
  .subtitle { font-weight: 700; font-size: 27px; color: var(--ink); letter-spacing: 1px; }
  .subtitle .lead { font-size: 24px; }
  .subtitle .skill { color: var(--green); font-size: 32px; font-weight: 900; margin-left: 8px; }
  .subtitle .power { color: var(--red); font-size: 32px; font-weight: 900; }

  .scene-photo { position: absolute; left: 0; top: 62px; width: 748px; height: 748px;
    background: linear-gradient(180deg, var(--photo-a), var(--photo-b)); }
  .figure { position: absolute; left: 40px; top: 140px; width: 360px; height: 670px;
    background: linear-gradient(180deg, var(--figure-a), var(--figure-b)); border-radius: 150px 150px 0 0; }

  .title { position: absolute; right: 14px; top: 74px; margin: 0; text-align: right;
    color: var(--navy); font-weight: 900; font-size: 40px; letter-spacing: 0; line-height: 1; }
  .title span { display: block; transform: scaleY(1.75); transform-origin: right top; height: 100px; }

  .author { position: absolute; left: 64px; top: 600px; margin: 0; writing-mode: vertical-rl;
    font-weight: 900; font-size: 34px; color: var(--navy); letter-spacing: 6px; }

  .bottom { position: absolute; left: 0; top: 808px; width: 748px; height: 392px; background: var(--navy); }
  .tagline { margin: 0; height: 58px; line-height: 58px; text-align: center; color: var(--white);
    font-weight: 900; font-size: 27px; background: var(--navy-deep); }
  .perks { display: flex; gap: 24px; padding: 14px 20px 0; }
  .perk { flex: 1; }
  .perk-label { margin: 0; background: var(--green); color: var(--white); font-weight: 700;
    font-size: 25px; height: 46px; line-height: 46px; padding-left: 14px; }
  .perk-body { margin: 0; background: var(--white); color: var(--navy); font-weight: 700; font-size: 24px;
    line-height: 1.45; height: 234px; box-sizing: border-box; padding: 22px 12px; text-align: center;
    display: flex; align-items: center; justify-content: center; }
</style>
</head>
<body>
<main class="cover">
  <header class="subtitle-band">
    <p class="subtitle"><span class="lead">未来をひらくのは</span><span class="skill">話術</span>より<span class="power">笑顔力</span></p>
  </header>

  <div class="scene-photo" role="img" aria-label="明るいオフィスのぼかし背景写真"></div>
  <div class="figure" role="img" aria-label="スーツ姿のビジネスマンのイラスト"></div>

  <h1 class="title">
    <span>どうして?腕時計を</span>
    <span>磨くと</span>
    <span>来店客がふえるのか</span>
  </h1>

  <p class="author">柚木野春人</p>

  <section class="bottom">
    <p class="tagline">理想の自分を作るためのヒントがここにある!</p>
    <div class="perks">
      <div class="perk">
        <p class="perk-label">読者特典①</p>
        <p class="perk-body">『失敗しないもの選び・マスコミでは出さないもの選びのポイント』</p>
      </div>
      <div class="perk">
        <p class="perk-label">読者特典②</p>
        <p class="perk-body">得たい成果を得る為の<br>５つのステップ<br>チェックシート</p>
      </div>
    </div>
  </section>
</main>
</body>
</html>
```